Business Card Design Project Massage Shop

Business card for Foot, Hot Stone and Full body Massage. I am thinking photo for the front. Back should say "$20 off 1hr basic service" "Offer not valid with any other coupons or offers"

Target Market(s)

Women wanting good quality massage

Industry/Entity Type

Business

Contact Information for Business Card

816.472.3908
27815 W 12 Hwy
Independence Mo 64055

www.lanternmassage.co

Other font styles liked:
• http://www.typequarry.net/fonts/brelwick/no.-seven/

Colors
0455a3

Requirements
Must have
• The business name "Lantern Massage" must be in this font and a royal blue color http://www.typequarry.net/fonts/brelwick/no.-seven/
• The remaining information must be more readable.
Should not have
• the web site is .co
• Not a .com
• should not look like it was done on a prindle or someothere website.

```html
<!DOCTYPE html>
<html lang="en">
<head>
<meta charset="utf-8">
<title>Lantern Massage – Business Card</title>
<link href="https://fonts.googleapis.com/css2?family=Bodoni+Moda:wght@500;700&display=swap" rel="stylesheet">
<style>
  :root {
    --backdrop: #e9e6e1;
    --card-white: #fbfbfb;
    --card-black: #060606;
    --royal-blue: #3b3a9c;
    --accent-purple: #7b4fa3;
    --badge-grey: #a39e97;
    --ink: #111111;
    --ink-soft: #444444;
    --text-on-dark: #f4f4f4;
  }
  * { box-sizing: border-box; margin: 0; padding: 0; }
  html, body {
    width: 1200px; height: 892px; overflow: hidden;
    background: var(--backdrop);
    font-family: "Bodoni Moda", "Didot", serif;
  }
  .canvas { position: relative; width: 1200px; height: 892px; }
  .card {
    position: absolute; left: 260px;
    width: 680px; height: 389px;
    background: var(--card-white);
    box-shadow: 0 6px 18px rgba(0,0,0,.18);
    overflow: hidden;
  }
  .card--front { top: 38px; }
  .card--back { top: 465px; }

  .front-shape { position: absolute; inset: 0; }

  .brand {
    position: absolute; left: 90px; top: 40px;
    color: var(--royal-blue);
    font-weight: 700; font-size: 52px; line-height: 1;
    white-space: nowrap;
  }
  .brand-badge {
    position: absolute; right: 30px; top: 148px;
    width: 96px; height: 96px; border-radius: 50%;
    background: var(--badge-grey);
    border: 6px solid var(--accent-purple);
  }
  .phone {
    position: absolute; left: 205px; top: 110px;
    font-weight: 700; font-size: 40px; color: var(--ink);
  }
  .web, .address {
    position: absolute; color: var(--text-on-dark);
    font-weight: 500; white-space: nowrap;
  }
  .web { left: 150px; top: 265px; font-size: 27px; }
  .address { left: 60px; top: 315px; font-size: 30px; }

  .card--back .brand { left: 60px; top: 60px; font-size: 64px; }
  .offer {
    position: absolute; left: 60px; right: 60px; top: 215px;
    font-weight: 700; font-size: 34px; line-height: 1.2; color: var(--ink);
    white-space: nowrap;
  }
  .terms {
    position: absolute; left: 60px; right: 60px; top: 290px;
    font-weight: 500; font-size: 20px; line-height: 1.3; color: var(--ink-soft);
    white-space: nowrap;
  }
</style>
</head>
<body>
<main class="canvas">
  <section class="card card--front" aria-label="Business card front">
    <svg class="front-shape" viewBox="0 0 680 389" width="680" height="389" aria-hidden="true">
      <polygon points="0,0 24,0 44,175 590,300 680,240 680,389 0,389" fill="var(--card-black)"/>
      <polyline points="38,0 58,165 592,284 680,226" fill="none" stroke="var(--royal-blue)" stroke-width="7"/>
    </svg>
    <div class="brand">Lantern Massage</div>
    <div class="brand-badge" aria-hidden="true"></div>
    <div class="phone">816.472.3908</div>
    <div class="web">www.lanternmassage.co</div>
    <div class="address">27815 W 12 Hwy Independence Mo 64055</div>
  </section>

  <section class="card card--back" aria-label="Business card back">
    <div class="brand">Lantern Massage</div>
    <p class="offer">$20 off next 1hr+ basic service</p>
    <p class="terms">Offer not valid with any other coupons or offers</p>
  </section>
</main>
</body>
</html>
```